Brindle Capital websites

We need a website design for a finance company based on Gold Coast. Basically need 4 homepages....one for their main website Brindle Capital Group and then 3 others all based on the same template for Brindle Lending, Brindle Invoicing and Brindle Debt Management.

Target Market(s)

Adults based in western speaking countries who require fast loans.

Industry/Entity Type

Financial

Number of Pages Required

4 pages

Requirements
Must have
• ? Brindle Capital Group are after 4 websites designed for the below:
o Brindle Capital Group Pty Ltd
o Brindle Lending Pty Ltd
o Brindle Debt Management Pty Ltd
o Brindle Invoicing Pty Ltd
Website 1 – Brindle Capital Group Pty Ltd
Overview
The Brindle Capital Group Pty Ltd website will act as the ‘fronting/summary site’ so should be kept as clean and simple as possible, very little text.
o The company name Brindle Capital Group and logo at the top (ATTACHED Brindlecapitalgrp_colored_shadow.jpg)
o Our phone number & email address at the top of the page also. (just use dummy ones for design)
o Perhaps a few lines under the phone number/email/logo etc explaining that Brindle Capital Group is the parent company to Brindle Lending, Brindle Invoicing and Brindle Debt Management.
o Then we just want three large, clear icons down the left hand side of the page. Each icon will be the logo of our businesses eg Brindle Lending, Brindle Debt Management and Brindle Invoicing (all logos are attached). There will then be a few lines next to the logo saying ‘Click here to go to Brindle Lending/Brindle Invoicing/Brindle Debt Management’, and a few lines about each company.
• Some icons and containers will be designed for homepage
? Brindle Lending (image/description/click here)
? Brindle Debt Management (image/description/click here)
? Brindle Invoicing (image/description/click here)

Website 2 – Brindle Lending Pty Ltd
Overview
We also require a separate site for each of the 3 businesses; ie a site for Brindle Lending, a site for Brindle Debt Management and a site for Brindle Invoicing. These sites need to be very easy to navigate, clear and professional looking. We would like them to look something like the screenshot below.
Site Map
• Home
• Frequently Asked Questions
• Corporate Information
• Promotions and Latest News
• Testimonials
• Careers
• Contact Us

• The bold logo in the left hand corner. It stands out.
• The core info below the logo (ie. phone number, email address etc)
• The tabs at the top of the page ‘home, corporate etc’
• The big space for an image (or series of images)
• The space under the picture for your body copy.
• Under the logo (in the strip down the left hand side of the page…or somewhere highly visible), we would like 2 big icons with the text ‘For loans over $5000, click here’ and ‘For loans under $5000, click here’). This needs to be the focus of this page!! This is very important. Then, once customers have clicked on either icon they will be taken through to an online form they need to complete. There will be 2 different forms – 1 for loans under $5000 and 1 for loans over $5000.
• We will definitely be inserting the logos of the companies we arrange loans for next to the body copy (as KWR have done above – see how they have OLT and other company’s logos inserted). We will not put too much copy here however as we really want the attention to be on the 2 icons mentioned above.
• We would like space for a large image (or series of images…not sure yet) under the tabs.
• Area at the bottom (down left side) of homepage a statement promoting other business eg. “Brindle Capital Group, your one-stop-shop for financial services. Want to know what else we can do for you? Click on the below icons to find out” (then insert the logos for the other businesses).
• Some icons will be designed for homepage
? For Loans over $5000, click here
? For Loans under $5000, click here

Website 3 – Brindle Debt Management Pty Ltd
Overview
We require a separate site for each of the 3 businesses; ie a site for Brindle Lending, a site for Brindle Debt Management and a site for Brindle Invoicing. These sites need to be very easy to navigate, clear and professional looking. We would like them to look something like the screenshot in the word doc.

Site Map
• Home
• Corporate Information
• Testimonials
• Careers
• Contact Us

Design/Content Brief
• Rest of area will be used for content.

Website 4 – Brindle Invoicing Pty Ltd
Overview

Site Map
• Home
• Corporate Information
• Testimonials
• Careers
• Contact Us

Design/Content Brief

```html
<!DOCTYPE html>
<html lang="en">
<head>
<meta charset="utf-8">
<title>Brindle Capital Group</title>
<link rel="stylesheet" href="https://fonts.googleapis.com/css2?family=Noto+Sans:wght@400;700&display=swap">
<style>
  :root {
    --page: #ffffff;
    --ink: #1c1c1c;
    --panel-top: #d4d4d4;
    --panel-bottom: #8f8f8f;
    --panel-edge: #5a5a5a;
    --rule: #7e7e7e;
    --intro-box: #b9b9b9;
    --bar-top: #5a5a5a;
    --bar-bottom: #161616;
    --label: #3f3f3f;
    --contact: #ffffff;
    --card: #e4e4e4;
    --card-text: #2e3a86;
    --link: #c8183f;
    --divider: #d9d9d9;
    --foot-top: #5b6aae;
    --foot-bottom: #2a3673;
    --foot-text: #6e78a8;
    --brand-navy: #1f2f73;
    --brand-lending: #8a1526;
    --brand-debt: #e0700f;
    --brand-invoicing: #1f7a2f;
  }
  * { box-sizing: border-box; margin: 0; padding: 0; }
  html, body { width: 1200px; height: 944px; overflow: hidden; background: var(--page); }
  body { font-family: "Noto Sans", Verdana, sans-serif; color: var(--ink); }
  .page { position: relative; width: 1200px; height: 944px; }

  .brand {
    position: absolute; display: flex; align-items: center; gap: 14px;
  }
  .brand-dot { flex: none; border-radius: 50%; }
  .brand-name { font-weight: 700; line-height: 1.1; }

  .brand--main { left: 36px; top: 110px; width: 350px; }
  .brand--main .brand-dot { width: 46px; height: 46px; background: var(--brand-navy); }
  .brand--main .brand-name { font-size: 30px; color: var(--brand-navy); }

  .contact-panel {
    position: absolute; left: 409px; top: 28px; width: 767px; height: 300px;
    border: 2px solid var(--panel-edge); border-radius: 6px 6px 0 0;
    background: linear-gradient(to bottom, var(--panel-top), var(--panel-bottom));
    padding: 12px 20px 0 18px;
  }
  .contact-label { font-size: 20px; color: var(--label); }
  .contact-phone { font-size: 40px; color: var(--contact); line-height: 1.1; margin-top: 1px; }
  .contact-email { font-size: 26px; color: var(--contact); line-height: 1.1; }
  .contact-rule { height: 3px; background: var(--rule); margin: 11px 0 16px; }
  .intro {
    background: var(--intro-box); padding: 6px 12px;
    font-size: 16px; line-height: 22px; color: var(--ink);
    height: 81px; overflow: hidden;
  }

  .header-bar {
    position: absolute; left: 19px; top: 321px; width: 1157px; height: 33px;
    border-radius: 5px;
    background: linear-gradient(to bottom, var(--bar-top), var(--bar-bottom));
  }

  .divisions { position: absolute; left: 0; top: 0; }
  .division-divider {
    position: absolute; top: 378px; width: 4px; height: 396px; background: var(--divider);
  }
  .division-brand { top: 470px; width: 324px; justify-content: center; }
  .division-brand .brand-dot { width: 40px; height: 40px; }
  .division-brand .brand-name { font-size: 27px; }
  .brand--lending .brand-dot { background: var(--brand-lending); }
  .brand--lending .brand-name { color: var(--brand-lending); }
  .brand--debt { top: 456px; }
  .brand--debt .brand-dot { background: var(--brand-debt); }
  .brand--debt .brand-name { color: var(--brand-debt); }
  .brand--invoicing .brand-dot { background: var(--brand-invoicing); }
  .brand--invoicing .brand-name { color: var(--brand-invoicing); }

  .division-card {
    position: absolute; top: 638px; height: 150px;
    background: var(--card); padding: 14px 16px;
  }
  .division-text { font-size: 16px; line-height: 21.5px; color: var(--card-text); white-space: nowrap; }
  .division-link {
    display: inline-block; margin-top: 10px;
    font-size: 22px; color: var(--link); text-decoration: none;
  }

  .site-footer {
    position: absolute; left: 24px; top: 853px; width: 1156px; height: 45px;
    border-radius: 6px;
    background: linear-gradient(to bottom, var(--foot-top), var(--foot-bottom));
    display: flex; align-items: center; justify-content: center;
    font-size: 13px; color: var(--foot-text);
  }
</style>
</head>
<body>
<div class="page">

  <header>
    <div class="brand brand--main">
      <span class="brand-dot"></span>
      <span class="brand-name">Brindle Capital Group</span>
    </div>

    <section class="contact-panel">
      <p class="contact-label">Phone</p>
      <p class="contact-phone">520 555 0142</p>
      <div class="contact-rule"></div>
      <p class="contact-label">E - mail</p>
      <p class="contact-email">info@brindlecapitalgroup.com.au</p>
      <div class="contact-rule"></div>
      <p class="intro">Lorem ipsum dolor sit amet, consectetur adipiscing elit. Integer feugiat, nisi in ullamcorper suscipit, justo justo luctus sapien, nec faucibus sapien nunc a diam. Morbi eu dolor quis justo vestibulum commodo. Praesent lacinia, dui sit amet ornare</p>
    </section>

    <div class="header-bar"></div>
  </header>

  <main class="divisions">
    <div class="division-divider" style="left:408px"></div>
    <div class="division-divider" style="left:782px"></div>

    <div class="brand division-brand brand--lending" style="left:58px">
      <span class="brand-dot"></span>
      <span class="brand-name">Brindle Lending</span>
    </div>
    <article class="division-card" style="left:58px; width:324px">
      <p class="division-text">Lorem ipsum dolor sit amet,<br>consectetur adipiscing elit. Integer<br>feugiat, nisi in ullamcorper<br>suscipit, justo justo luctus sapien,</p>
      <a class="division-link" href="#">Click here »</a>
    </article>

    <div class="brand division-brand brand--debt" style="left:434px">
      <span class="brand-dot"></span>
      <span class="brand-name">Brindle Debt<br>Management</span>
    </div>
    <article class="division-card" style="left:434px; width:324px">
      <p class="division-text">Lorem ipsum dolor sit amet,<br>consectetur adipiscing elit. Integer<br>feugiat, nisi in ullamcorper<br>suscipit, justo justo luctus sapien,</p>
      <a class="division-link" href="#">Click here »</a>
    </article>

    <div class="brand division-brand brand--invoicing" style="left:822px">
      <span class="brand-dot"></span>
      <span class="brand-name">Brindle Invoicing</span>
    </div>
    <article class="division-card" style="left:810px; width:349px">
      <p class="division-text">Lorem ipsum dolor sit amet,<br>consectetur adipiscing elit. Integer<br>feugiat, nisi in ullamcorper<br>suscipit, justo justo luctus sapien,</p>
      <a class="division-link" href="#">Click here »</a>
    </article>
  </main>

  <footer class="site-footer">Copyright © 2009 &nbsp;Brindle Capital Group</footer>

</div>
</body>
</html>
```